New Website Design for Rides for Heroes.org - A Site for People to Donate Cars to War / Disabled Ve

Current site: www.ridesforheroes.org; Look at these sites for ideas: bikez2tots.org; gearsforhopes.org; www.autosformarines.org; www.trucksforsoldiers.org

Industry/Entity Type

Charity

Coding

Coded - Design and coding required

Number of Pages Required

1 page

Requirements
Must have
• n/a
Nice to have
• n/a
Should not have
• n/a

```html
<!DOCTYPE html>
<html lang="en">
<head>
<meta charset="utf-8">
<title>Rides for Heroes – Donate Your Car</title>
<link href="https://fonts.googleapis.com/css2?family=Open+Sans:wght@400;600;700;800&display=swap" rel="stylesheet">
<style>
:root{
  --orange:#f26b3a;
  --dark:#2b3640;
  --darker:#222b33;
  --ink:#2a2a2a;
  --grey:#666;
  --light:#f3f3f3;
  --line:#d5d5d5;
  --white:#fff;
}
*{box-sizing:border-box;margin:0;padding:0}
html,body{width:1200px;height:3243px;overflow:hidden}
body{font-family:"Open Sans",Arial,sans-serif;color:var(--ink);background:var(--white);position:relative}
section,header,footer{position:absolute;left:0;width:1200px}
.abs{position:absolute}
.btn{position:absolute;display:flex;align-items:center;justify-content:center;font-weight:700;font-size:14px;color:var(--white);background:var(--orange)}
.btn.dark{background:var(--dark)}

/* top bar */
.topbar{top:0;height:37px;background:var(--dark)}
.social{left:72px;top:10px;display:flex;gap:6px}
.social span{width:17px;height:17px;border-radius:50%;background:#6d7a84;display:block}
.contact{right:72px;top:0;height:37px;display:flex;gap:24px;align-items:center;color:#dfe4e8;font-size:12px}
.contact span{display:flex;align-items:center;gap:6px}
.contact svg{width:14px;height:14px;fill:#dfe4e8}

/* header */
.site-header{top:37px;height:114px;background:var(--white)}
.brand{left:88px;top:30px;display:flex;align-items:center;gap:8px}
.brand .mark{width:30px;height:30px;border-radius:50%;background:var(--orange)}
.brand .name{font-size:22px;font-weight:700;color:var(--orange);line-height:1}
.brand .tag{position:absolute;left:38px;top:30px;font-size:11px;color:var(--ink);white-space:nowrap}
.nav{right:70px;top:43px;display:flex;gap:8px}
.nav a{font-size:13px;font-weight:700;color:var(--ink);text-decoration:none;padding:6px 10px;border:2px solid transparent;text-transform:uppercase}
.nav a.active{border-color:var(--orange)}

/* hero */
.hero{top:151px;height:461px;background:linear-gradient(90deg,#b7a38b 0%,#c9b79f 40%,#9c8f7c 70%,#6f8a4e 100%)}
.hero-text{left:700px;top:135px;color:var(--ink)}
.hero-text .kicker{font-size:24px;font-weight:600;letter-spacing:.5px}
.hero-text h1{font-size:56px;font-weight:800;line-height:1.05;letter-spacing:1px}
.hero-text .sub{font-size:21px;font-weight:700;margin-top:6px}
.hero-text .sub em{font-style:normal;color:var(--orange)}
.hero .btn{left:713px;top:272px;width:150px;height:44px;font-size:16px}
.arrow{width:0;height:0;border-top:10px solid transparent;border-bottom:10px solid transparent}
.arrow.next{right:26px;top:202px;border-left:13px solid #111}
.arrow.prev{left:26px;top:202px;border-right:13px solid rgba(0,0,0,.25)}

/* donate band */
.donate{top:612px;height:274px;background:#2e3a42;color:var(--white)}
.donate h2{position:absolute;top:22px;width:100%;text-align:center;font-size:28px;font-weight:700}
.vehicles{left:443px;top:80px;width:375px;height:66px;background:var(--white);display:flex;border:1px solid #ccc}
.vehicles div{flex:1;border-right:1px solid #ddd;display:flex;flex-direction:column;align-items:center;justify-content:center;gap:4px;font-size:10px;color:#555}
.vehicles div:last-child{border-right:0}
.vehicles div.on{background:#e6e6e6;font-weight:700;color:#222}
.vehicles svg{width:36px;height:24px;fill:none;stroke:#444;stroke-width:1.6}
.field-label{font-size:17px;top:172px}
.select{top:203px;height:43px;background:var(--white);color:#999;font-size:13px;padding:0 10px;display:flex;align-items:center}
.select::after{content:"";position:absolute;right:0;top:0;width:32px;height:43px;border-left:1px solid #ddd;background:linear-gradient(#fff,#fff)}
.select i{position:absolute;right:11px;top:18px;width:0;height:0;border-left:5px solid transparent;border-right:5px solid transparent;border-top:7px solid #555;z-index:1}
.donate .btn{left:980px;top:203px;width:147px;height:43px;font-size:15px}

/* story */
.story{top:886px;height:329px;background:var(--white);text-align:center}
.story h2{position:absolute;top:42px;width:100%;font-size:26px;font-weight:700}
.story p{position:absolute;left:100px;width:1000px;top:104px;font-size:12.5px;line-height:22px;color:var(--grey)}
.story hr{position:absolute;left:435px;width:330px;top:190px;border:0;border-top:1px solid #999}
.story .btn{top:227px;height:52px;width:172px;font-size:15px}

/* features */
.features{top:1215px;height:406px;background:var(--light)}
.card{top:29px;width:248px;height:345px;text-align:center}
.card.featured{background:var(--orange);color:var(--white)}
.card .icon{position:absolute;left:56px;top:31px;width:136px;height:100px;background:var(--dark);display:flex;align-items:center;justify-content:center}
.card.featured .icon{background:var(--white)}
.card .icon svg{width:58px;height:50px}
.card h3{position:absolute;top:178px;width:100%;font-size:15px;font-weight:700}
.card p{position:absolute;top:206px;left:30px;width:188px;font-size:12px;line-height:16px;color:#444}
.card.featured p{color:var(--white)}
.card .btn{left:70px;top:274px;width:108px;height:45px;font-size:13px}
.card.featured .btn{background:var(--darker)}

/* news & faq */
.news{top:1621px;height:595px;background:var(--white)}
.sec-title{font-size:27px;font-weight:800;letter-spacing:.5px}
.sec-title::after{content:"";display:block;width:52px;height:4px;background:var(--orange);margin-top:6px}
.news-photo{left:69px;top:112px;width:530px;height:276px;background:linear-gradient(160deg,#b9b3a6,#8b8a6e 50%,#5e5a46)}
.news-caption{left:69px;top:388px;width:530px;height:119px;background:var(--dark);color:var(--white)}
.date{position:absolute;left:20px;top:26px;width:52px;height:62px;background:var(--orange);text-align:center;color:var(--white);font-size:22px;line-height:30px;padding-top:4px}
.date small{display:block;font-size:11px;line-height:12px}
.news-caption p{position:absolute;left:82px;top:24px;width:420px;font-size:15px;line-height:22px}
.dots{display:flex;gap:5px}
.dots span{width:8px;height:8px;border-radius:50%;background:#ccc}
.dots span.on{background:#555}
.faq{left:668px;top:116px;width:453px}
.faq .q{height:44px;background:#ececec;font-size:14px;color:#444;display:flex;align-items:center;gap:8px;padding-left:14px;margin-bottom:2px}
.faq .q.hl{color:var(--orange)}
.faq .q b{display:inline-block;width:12px;height:12px;border:1px solid #777;font-size:10px;line-height:9px;text-align:center;font-weight:400}
.faq .a{height:252px;background:#f7f7f7;padding:42px 24px;text-align:center;font-size:12.5px;line-height:20px;color:#999;margin-bottom:2px}

/* testimonial */
.testimonial{top:2216px;height:476px;background:linear-gradient(180deg,#4e5a3c,#6b6d52 55%,#8a7b63);color:var(--white)}
.testimonial h2{position:absolute;top:72px;width:100%;text-align:center;font-size:28px;font-weight:800}
.testimonial h2 span{color:var(--orange)}
.quote{left:200px;top:150px;width:803px;height:115px;background:rgba(30,30,30,.78);text-align:center;font-size:12.5px;line-height:22px;padding:22px 40px}
.avatar{left:600px;top:274px;width:70px;height:70px;background:#b7bcc2;border:2px solid #eee}
.who{top:352px;width:100%;text-align:center;font-size:13px;line-height:22px}
.who span{color:var(--orange)}

/* signup */
.signup{top:2692px;height:212px;background:#ebe7e5;text-align:center}
.signup h2{position:absolute;top:40px;width:100%;font-size:27px;font-weight:700}
.signup .sub{position:absolute;top:82px;width:100%;font-size:14px;color:var(--orange)}
.input{top:139px;height:41px;background:var(--white);border:1px solid #ccc;font-size:13px;color:#999;padding:0 12px;display:flex;align-items:center}
.signup .btn{left:832px;top:139px;width:108px;height:41px;background:var(--dark)}

/* footer */
.site-footer{top:2904px;height:300px;background:var(--dark);color:var(--white)}
.site-footer h4{font-size:19px;font-weight:700;position:absolute;top:22px}
.links{position:absolute;top:72px;list-style:none;font-size:11.5px;line-height:21.5px;color:#dfe4e8}
.links li::before{content:"";display:inline-block;width:4px;height:4px;background:var(--orange);margin:0 10px 2px 0}
.f-brand{left:72px;top:72px;display:flex;align-items:center;gap:8px}
.f-brand .mark{width:26px;height:26px;border-radius:50%;background:var(--orange)}
.f-brand .name{font-size:20px;font-weight:700;color:var(--orange)}
.f-about{left:70px;top:160px;width:190px;font-size:11.5px;line-height:19px;text-align:center;color:#dfe4e8}
.f-input{background:var(--white);color:#999;font-size:11px;padding:0 8px;display:flex;align-items:center;left:930px;width:200px}
.site-footer .btn{left:930px;top:226px;width:85px;height:34px}
.copyright{position:absolute;left:0;top:3204px;width:1200px;height:39px;background:var(--darker);color:#dfe4e8;font-size:12px;text-align:center;line-height:39px}
.copyright .sq{position:absolute;top:11px;width:18px;height:18px;background:#5a6a78}
</style>
</head>
<body>

<div class="topbar abs" style="width:1200px;left:0">
  <div class="social abs"><span></span><span></span><span></span><span></span><span></span></div>
  <div class="contact abs">
    <span><svg viewBox="0 0 24 24"><path d="M6.6 10.8a15.1 15.1 0 0 0 6.6 6.6l2.2-2.2a1 1 0 0 1 1-.25 11.4 11.4 0 0 0 3.6.57 1 1 0 0 1 1 1V20a1 1 0 0 1-1 1A17 17 0 0 1 3 4a1 1 0 0 1 1-1h3.5a1 1 0 0 1 1 1c0 1.25.2 2.45.57 3.57a1 1 0 0 1-.25 1z"/></svg>+1 555-014-2290</span>
    <span><svg viewBox="0 0 24 24"><path d="M2 5h20v14H2z M2 5l10 8 10-8" fill="none" stroke="#dfe4e8" stroke-width="2"/></svg>WebMail</span>
    <span><svg viewBox="0 0 24 24"><path d="M3 4h18v12H8l-5 4z"/></svg>LiveChat</span>
    <span><svg viewBox="0 0 24 24"><circle cx="12" cy="12" r="9" fill="none" stroke="#dfe4e8" stroke-width="2"/><circle cx="12" cy="12" r="4"/></svg>Support</span>
  </div>
</div>

<header class="site-header">
  <div class="brand abs"><span class="mark"></span><span class="name">Rides for Heroes</span><span class="tag">Donates Your Cars Us</span></div>
  <nav class="nav abs">
    <a class="active" href="#">Home</a><a href="#">Why Us</a><a href="#">FAQ</a><a href="#">Donate a Car</a><a href="#">Our Charity</a><a href="#">About Us</a>
  </nav>
</header>

<section class="hero" role="img" aria-label="Photo of a smiling soldier in uniform holding two young children outside a house">
  <span class="arrow prev abs"></span>
  <div class="hero-text abs">
    <div class="kicker">CAR DONATION MADE EASY!</div>
    <h1>VETRANS</h1>
    <div class="sub">Takes 2 minutes. <em>Join our 400,000+</em></div>
  </div>
  <a class="btn" href="#">About Us</a>
  <span class="arrow next abs"></span>
</section>

<section class="donate">
  <h2>DONATE CAR US!</h2>
  <div class="vehicles abs">
    <div class="on"><svg viewBox="0 0 36 24"><circle cx="8" cy="16" r="5"/><circle cx="28" cy="16" r="5"/><path d="M8 16l7-7h8l5 7M15 9l4-4"/></svg>MotorCycle</div>
    <div><svg viewBox="0 0 36 24"><path d="M3 15h30l-4 6H7zM10 15V8h14v7M14 8V4h6v4"/></svg>Boat/PWC</div>
    <div><svg viewBox="0 0 36 24"><path d="M3 17v-5l5-6h18l6 6v5zM3 12h29"/><circle cx="10" cy="18" r="3"/><circle cx="26" cy="18" r="3"/></svg>Car</div>
    <div><svg viewBox="0 0 36 24"><path d="M6 19V4h16l6 7v8zM22 4v7h6"/><circle cx="11" cy="19" r="3"/><circle cx="24" cy="19" r="3"/></svg>RV</div>
    <div><svg viewBox="0 0 36 24" style="stroke:none;fill:#444"><circle cx="10" cy="12" r="2.2"/><circle cx="18" cy="12" r="2.2"/><circle cx="26" cy="12" r="2.2"/></svg>Others</div>
  </div>
  <span class="field-label abs" style="left:69px">What kind of car?</span>
  <span class="field-label abs" style="left:522px">Mileage</span>
  <span class="field-label abs" style="left:667px">Does it run?</span>
  <span class="field-label abs" style="left:811px">Have the title?</span>
  <div class="select abs" style="left:69px;width:143px">Make...<i></i></div>
  <div class="select abs" style="left:220px;width:143px">Year...<i></i></div>
  <div class="select abs" style="left:370px;width:143px">Model...<i></i></div>
  <div class="select abs" style="left:522px;width:140px">Select...<i></i></div>
  <div class="select abs" style="left:670px;width:142px">Select...<i></i></div>
  <div class="select abs" style="left:823px;width:143px">Yes<i></i></div>
  <a class="btn" href="#">Donate NOW!</a>
</section>

<section class="story">
  <h2>OUR STORY</h2>
  <p>Our car donation program was born of a single brainstorm we had back in 1994. Rather than rely on private donations and traditional fundraising methods to support our growing charity, we'd provide a public service that would send a steady stream of revenue directly to our charity programs. We also made the decision to process all car donations in house, allowing the full proceeds of each donation to go directly to our charity programs.</p>
  <hr>
  <a class="btn dark" href="#" style="left:435px">LEARN MORE</a>
  <a class="btn" href="#" style="left:618px">ABOUT US</a>
</section>

<section class="features">
  <div class="card featured abs" style="left:71px">
    <div class="icon"><svg viewBox="0 0 58 50"><path d="M4 14h30v22H4zM34 22h10l8 8v6H34z" fill="var(--dark)"/><circle cx="14" cy="38" r="5" fill="var(--dark)" stroke="#fff" stroke-width="2"/><circle cx="44" cy="38" r="5" fill="var(--dark)" stroke="#fff" stroke-width="2"/><text x="19" y="29" font-size="9" font-weight="700" fill="#fff" text-anchor="middle" font-family="Open Sans,Arial,sans-serif">FREE</text></svg></div>
    <h3>FAST AND FREE PICKUP</h3>
    <p>Your car donation can be picked up within 24 hours - or even same day if needed.</p>
    <a class="btn" href="#">Read More...</a>
  </div>
  <div class="card abs" style="left:341px">
    <div class="icon"><svg viewBox="0 0 58 50" fill="none" stroke="#fff" stroke-width="2"><circle cx="22" cy="28" r="13"/><text x="22" y="34" font-size="16" fill="#fff" stroke="none" text-anchor="middle" font-family="Open Sans,Arial,sans-serif">$</text><ellipse cx="42" cy="14" rx="9" ry="3"/><path d="M33 14v14c0 2 4 3 9 3s9-1 9-3V14M33 21c0 2 4 3 9 3s9-1 9-3"/></svg></div>
    <h3>SAVE MONEY ON YOUR TAXES</h3>
    <p>Your car donation can be picked up within 24 hours - or even same day if needed.</p>
    <a class="btn" href="#">Read More...</a>
  </div>
  <div class="card abs" style="left:627px">
    <div class="icon"><svg viewBox="0 0 58 50" fill="#fff"><path d="M28 18c0 10-2 20-6 26h5c3-7 4-16 3-26z"/><path d="M29 18c-6-6-14-6-18-2 6-1 11 0 18 2zM29 18c4-7 12-9 17-6-6 0-11 2-17 6zM29 18c7-2 14 1 16 6-5-3-10-4-16-6zM29 18c-5 1-10 5-11 10 3-4 7-7 11-10z"/><path d="M8 44h40v2H8z"/></svg></div>
    <h3>VACATION VOUCHER</h3>
    <p>Your car donation can be picked up within 24 hours - or even same day if needed.</p>
    <a class="btn" href="#">Read Move...</a>
  </div>
  <div class="card abs" style="left:897px">
    <div class="icon"><svg viewBox="0 0 58 50" fill="none" stroke="#fff" stroke-width="2"><rect x="17" y="8" width="24" height="34" rx="5"/><path d="M17 20h24M20 14h18M21 34h2M35 34h2M19 42v4M39 42v4"/></svg></div>
    <h3>FAST AND FREE PICKUP</h3>
    <p>Your car donation can be picked up within 24 hours - or even same day if needed.</p>
    <a class="btn" href="#">Read More...</a>
  </div>
</section>

<section class="news">
  <div class="sec-title abs" style="left:69px;top:50px">LATEST NEWS</div>
  <div class="news-photo abs" role="img" aria-label="Photo of two armed soldiers in camouflage talking on a city street"></div>
  <div class="news-caption abs">
    <div class="date">06<small>Feb</small></div>
    <p>Your car donation can be picked up within 24 hours - or even same day if needed.Your car donation</p>
  </div>
  <div class="dots abs" style="left:295px;top:532px"><span></span><span class="on"></span><span></span><span></span><span></span></div>

  <div class="sec-title abs" style="left:668px;top:50px">HAVE QUESTIONS?</div>
  <div class="faq abs">
    <div class="q"><b>−</b>How do I cancel and delete my account?</div>
    <div class="a">You can cancel or close your website and account at any time. To do so, login to HostPanel with your email/password combination. Your sites will be listed on your dashboard. Click the "delete site" link to delete a website. If you are logging in with a username/password combination, then login, and click on the "Site Settings" link. You will find a delete account link at the bottom right of the Site Settings page.You will find a delete account link at the bottom right of the Site Settings page.</div>
    <div class="q"><b>+</b>How do I cancel and delete my account?</div>
    <div class="q"><b>+</b>How do I cancel and delete my account?</div>
    <div class="q hl"><b style="border-color:var(--orange)">+</b>How do I cancel and delete my account?</div>
  </div>
</section>

<section class="testimonial" role="img" aria-label="Photo of armoured military vehicles and soldiers on a dirt road lined with trees">
  <h2>DONATORS <span>TESTIMONIAL</span></h2>
  <div class="quote abs">Lorem ipsum dolor sit amet, consectetur adipiscing elit. Donec lacus nibh, vulputate eu diam non, sodales tincidunt ligula. Pellentesque molestie nisi in dolor gravida commodo. Lorem ipsum dolor sit amet, consectetur adipiscing elit. Donec lacus nibh, vulputate eu diam non, sodales tincidunt ligula ellentesque molestie nisi in dolor</div>
  <div class="avatar abs" role="img" aria-label="Portrait photo of the reviewer"></div>
  <div class="who abs">Dana Morrow<br>CEO <span>Tusk Themes</span></div>
  <div class="dots abs" style="left:615px;top:424px"><span style="background:var(--orange)"></span><span style="background:#fff"></span><span style="background:#fff"></span><span style="background:#fff"></span></div>
</section>

<section class="signup">
  <h2>SIGN UP BELOW TO GET NEWS</h2>
  <div class="sub">SUBSCRIBE TO OUR MAILING LIST</div>
  <div class="input abs" style="left:359px;width:227px">Your Name</div>
  <div class="input abs" style="left:596px;width:227px">Your Email</div>
  <a class="btn" href="#">Send Us</a>
</section>

<footer class="site-footer">
  <h4 style="left:70px">About Us</h4>
  <div class="f-brand abs"><span class="mark"></span><span class="name">Rides for Heroes</span></div>
  <div class="abs" style="left:106px;top:104px;font-size:11px;color:#dfe4e8">Donates Your Cars Us</div>
  <p class="f-about abs">Aquam est tortor, sagittis in fringilla in, pellent esque nec erat. Aenean semper, neque non faucibus. tortor, sagittis in fringilla in, pellent esque nec eratsemper, neque non.</p>

  <h4 style="left:329px">Our Services</h4>
  <ul class="links" style="left:338px"><li>Website Builder</li><li>Web Design</li><li>Logo Design</li><li>Register Domains</li><li>Traffic Booster</li><li>Search Advertising</li><li>Email Marketing</li></ul>

  <h4 style="left:530px">Company</h4>
  <ul class="links" style="left:538px"><li>About BrightHost</li><li>Awards Reviews</li><li>Press Media</li><li>Company Blog</li><li>Contact Us</li><li>Carrers</li></ul>

  <h4 style="left:722px">Quick Links</h4>
  <ul class="links" style="left:730px"><li>About BrightHost</li><li>Awards Reviews</li><li>Press Media</li><li>Company Blog</li><li>Contact Us</li><li>Carrers</li></ul>

  <h4 style="left:923px">Connect With Us</h4>
  <div class="f-input abs" style="top:70px;height:34px">Your Name</div>
  <div class="f-input abs" style="top:110px;height:34px">Your Email</div>
  <div class="f-input abs" style="top:150px;height:68px;align-items:flex-start;padding-top:8px">Message</div>
  <a class="btn" href="#">Send</a>
</footer>

<div class="copyright">© 2015 Rides for Heroes All Right Reserved.
  <span class="sq" style="left:1030px"></span><span class="sq" style="left:1052px"></span><span class="sq" style="left:1074px"></span><span class="sq" style="left:1096px"></span>
</div>

</body>
</html>
```